Brellow Publishing

I made a website myself www.brellowpublishing.co.uk a few years ago but I need a new design, which I will code. One that I can be proud of, that 's sexy, to win new customers and showcase my publishing skills. This is a publishing website so I want the home page and books page to be fantastic. I have a logo already so will like the same colour scheme or thereabouts. I have current files and features that I would like to add to your creativity and experience.

Target Market(s)

Web Designers, Graphic Designers

Industry/Entity Type

Book Publisher

Number of Pages Required

5+ page

Font styles to use
Sans Serif

Colors
0255a3
ffffff
ec1f27

Requirements
Must have
• Menu and Sub Menu
• Footer
• Buy Page - Shopping Cart
• Upload feature on the submissions page
• video section on home page (how we publish books)
• Ad space section
Nice to have
• social media bar
• Zoom in page

```html
<!DOCTYPE html>
<html lang="en">
<head>
<meta charset="utf-8">
<title>Brellow Publishing</title>
<link href="https://fonts.googleapis.com/css2?family=Lato:wght@300;400;700&display=swap" rel="stylesheet">
<style>
:root{
  --navy:#1e1664;
  --red:#ff1a12;
  --brand-red:#ec1f27;
  --green:#8cc63f;
  --grey:#d6d6d6;
  --ink:#2b2b2b;
  --white:#ffffff;
  --rule:#c9c9d6;
}
*{box-sizing:border-box;margin:0;padding:0}
html,body{width:1200px;height:3711px;overflow:hidden}
body{font-family:'Lato',sans-serif;color:var(--ink);background:var(--white);position:relative}

/* header */
.site-header{position:absolute;left:0;top:0;width:1200px;height:104px;border-bottom:2px solid var(--rule)}
.brand{position:absolute;left:40px;top:34px}
.brand-name{font-size:30px;font-weight:700;color:var(--navy);display:flex;align-items:center;gap:12px;white-space:nowrap}
.brand-name::before{content:"";width:26px;height:26px;border-radius:50%;background:var(--brand-red)}
.search{position:absolute;left:656px;top:35px;width:259px;height:34px;border:2px solid #bbb;background:#fff}
.search-btn{position:absolute;right:-2px;top:-2px;width:34px;height:34px;background:#333}
.social{position:absolute;left:930px;top:33px;display:flex;gap:6px}
.social span{width:40px;height:40px}
.nav{position:absolute;left:0;top:104px;width:1200px;height:77px;display:flex;justify-content:space-between;align-items:center;padding:0 42px;border-bottom:1px solid var(--rule)}
.nav a{font-size:19px;color:var(--navy);text-decoration:none;letter-spacing:.5px}

/* hero */
.hero{position:absolute;left:0;top:181px;width:1200px;height:653px;
  background:linear-gradient(120deg,#d9d4cf 0%,#f1efed 35%,#8a8d94 60%,#4a3a33 80%,#e6e4e2 100%)}
.hero-title{position:absolute;left:40px;top:100px;font-size:70px;font-weight:300;color:var(--white);white-space:nowrap}
.hero-cta{position:absolute;left:480px;top:195px;display:flex;align-items:center;gap:14px;font-size:34px;color:var(--white);font-weight:300;white-space:nowrap}
.round-arrow{width:42px;height:42px}
.hero .prev{position:absolute;left:41px;top:318px}
.hero .next{position:absolute;left:1117px;top:318px}

/* intro */
.intro{position:absolute;left:0;top:834px;width:1200px;height:576px;background:var(--navy);color:var(--white);text-align:center}
.intro h2{position:absolute;top:52px;width:100%;font-size:46px;font-weight:400;line-height:58px}
.intro p{position:absolute;top:177px;left:250px;width:700px;font-size:22px;line-height:29px}
.feature{position:absolute;top:324px;width:144px;text-align:center}
.feature-icon{width:144px;height:144px;border-radius:50%;background:var(--white);display:flex;align-items:center;justify-content:center}
.feature-label{margin-top:26px;font-size:22px;letter-spacing:.5px;white-space:nowrap}

/* steps */
.steps-title{position:absolute;top:1430px;width:1200px;text-align:center;font-size:46px;font-weight:400;color:#333}
.step{position:absolute;top:1517px;width:257px;height:408px;border:2px solid var(--navy);border-radius:4px;padding:18px 16px}
.step h3{display:flex;align-items:center;gap:8px;font-size:33px;font-weight:400;color:var(--navy);white-space:nowrap}
.step-num{flex:0 0 42px;width:42px;height:42px;border-radius:50%;background:var(--navy);color:#fff;font-size:28px;font-weight:700;display:flex;align-items:center;justify-content:center}
.step p{margin-top:14px;font-size:17px;line-height:22px;color:#444;padding:0 4px}
.step p + p{margin-top:22px}

/* new season */
.season{position:absolute;left:0;top:1992px;width:1200px;height:499px;background:var(--grey)}
.season h2{position:absolute;top:28px;width:100%;text-align:center;font-size:46px;font-weight:400;color:#333}
.cover{position:absolute;box-shadow:2px 2px 4px rgba(0,0,0,.3)}
.season .prev{position:absolute;left:39px;top:253px}
.season .next{position:absolute;left:1116px;top:253px}

/* testimonials */
.testimonials{position:absolute;left:0;top:2491px;width:1200px;height:428px;background:var(--green);color:var(--white)}
.testimonials h2{position:absolute;top:34px;width:100%;text-align:center;font-size:46px;font-weight:400}
.quote{position:absolute;top:128px;width:400px}
.quote-head{display:flex;align-items:center;gap:22px;margin-left:3px}
.avatar{width:84px;height:84px;border-radius:50%;background:var(--white);position:relative;overflow:hidden}
.avatar::after{content:"";position:absolute;left:17px;top:20px;width:50px;height:70px;border-radius:25px 25px 0 0;background:#7fb6cf}
.quote-name{font-size:22px;font-weight:700;line-height:28px}
.quote p{margin-top:26px;font-size:23px;line-height:30px;font-weight:700}

/* partners */
.video{position:absolute;left:42px;top:3003px;width:416px;height:275px;border:3px solid var(--navy);
  background:linear-gradient(135deg,#e9e1d4,#b8a27a 40%,#6c5a8c 65%,#efe7da)}
.video .play{position:absolute;left:168px;top:98px}
.video-caption{position:absolute;left:42px;top:3292px;width:416px;text-align:center;font-size:28px;color:var(--navy)}
.partners-title{position:absolute;left:540px;top:2993px;width:630px;text-align:center;font-size:46px;font-weight:400;color:#333}
.partner{position:absolute;width:260px;text-align:center;font-size:32px;font-weight:700;color:#333;white-space:nowrap}

/* footer */
.site-footer{position:absolute;left:0;top:3390px;width:1200px;height:321px;background:var(--red);color:var(--white)}
.footer-brand{position:absolute;left:58px;top:100px;width:180px;text-align:center;font-size:26px;font-weight:700;line-height:32px}
.footer-brand::before{content:"";display:block;width:30px;height:30px;border-radius:50%;background:var(--white);margin:0 auto 12px}
.footer-col{position:absolute;top:84px;list-style:none;font-size:30px;line-height:40px;letter-spacing:.5px;white-space:nowrap}
</style>
</head>
<body>

<header class="site-header">
  <div class="brand">
    <div class="brand-name">Brellow Publishing</div>
  </div>
  <div class="search"><div class="search-btn">
    <svg width="34" height="34" viewBox="0 0 34 34"><circle cx="15" cy="15" r="6" fill="none" stroke="#fff" stroke-width="3"/><line x1="19.5" y1="19.5" x2="25" y2="25" stroke="#fff" stroke-width="3"/></svg>
  </div></div>
  <div class="social" aria-label="Social links">
    <span style="background:#3b5998"></span>
    <span style="background:#2aa3ef"></span>
    <span style="background:#d34836"></span>
    <span style="background:#0e76a8"></span>
    <span style="background:#c8232c"></span>
  </div>
</header>

<nav class="nav">
  <a>HOME</a><a>PUBLISHING</a><a>SUBMISSIONS</a><a>BOOKS</a><a>AUTHORS</a><a>SEMINARS</a><a>CONTACT</a>
</nav>

<section class="hero" role="img" aria-label="Photo of a smiling woman typing on a laptop">
  <h1 class="hero-title">Self-Publishing That Works</h1>
  <div class="hero-cta">
    <svg class="round-arrow" viewBox="0 0 42 42"><circle cx="21" cy="21" r="21" fill="#fff"/><path d="M17 12l9 9-9 9" fill="none" stroke="#8a8d94" stroke-width="4"/></svg>
    Submit Your Book
  </div>
  <svg class="round-arrow prev" viewBox="0 0 42 42"><circle cx="21" cy="21" r="21" fill="#1e1664"/><path d="M24 13l-8 8 8 8" fill="none" stroke="#fff" stroke-width="4"/></svg>
  <svg class="round-arrow next" viewBox="0 0 42 42"><circle cx="21" cy="21" r="21" fill="#1e1664"/><path d="M18 13l8 8-8 8" fill="none" stroke="#fff" stroke-width="4"/></svg>
</section>

<section class="intro">
  <h2>Have a Story to Tell?<br>We can help you publish your book.</h2>
  <p>Welcome to Brellow Publishing. We are an independent publishing company located in Leeds / York. We publish Trade (fiction and non-fiction), and Young Adult (YA) in a variety of subjects.</p>
  <div class="feature" style="left:190px">
    <div class="feature-icon"><svg width="70" height="86" viewBox="0 0 70 86"><rect x="4" y="2" width="62" height="82" rx="8" fill="#1e1664"/><rect x="12" y="70" width="50" height="8" fill="#fff"/><rect x="8" y="2" width="6" height="70" fill="#2e2680"/></svg></div>
    <div class="feature-label">BOOKS</div>
  </div>
  <div class="feature" style="left:527px">
    <div class="feature-icon"><svg width="84" height="74" viewBox="0 0 84 74"><rect x="20" y="4" width="44" height="26" fill="none" stroke="#1e1664" stroke-width="5"/><line x1="28" y1="14" x2="56" y2="14" stroke="#1e1664" stroke-width="3"/><line x1="28" y1="21" x2="56" y2="21" stroke="#1e1664" stroke-width="3"/><rect x="4" y="30" width="76" height="40" rx="6" fill="#1e1664"/><g fill="#fff"><circle cx="18" cy="42" r="3"/><circle cx="30" cy="42" r="3"/><circle cx="42" cy="42" r="3"/><circle cx="54" cy="42" r="3"/><circle cx="66" cy="42" r="3"/><rect x="22" y="54" width="40" height="6"/></g></svg></div>
    <div class="feature-label">AUTHORS</div>
  </div>
  <div class="feature" style="left:876px">
    <div class="feature-icon"><svg width="70" height="86" viewBox="0 0 70 86"><path d="M6 14h40l18 18v50H6z" fill="#1e1664"/><path d="M46 14v18h18" fill="#fff" opacity=".5"/><path d="M35 34l-16 16h10v18h12V50h10z" fill="#fff"/></svg></div>
    <div class="feature-label">SUBMISSIONS</div>
  </div>
</section>

<h2 class="steps-title">Publish Your Book in 4 Easy Steps</h2>
<article class="step" style="left:20px">
  <h3><span class="step-num">1</span>Writing</h3>
  <p>Lorem ipsum dolor sit amet, consectetur adipiscing elit. Morbi ultricies molestie orci.</p>
  <p>Aenean purus mauris, sodales nec diam dignissim, porttitor laoreet enim. Aliquam id sollicitudin turpis.</p>
  <p>Vivamus aliquet elit sem, et ornare ex aliquam in.</p>
</article>
<article class="step" style="left:324px">
  <h3><span class="step-num">2</span>Submission</h3>
  <p>Aenean purus mauris, sodales nec diam dignissim, porttitor laoreet enim.</p>
  <p>Aliquam id sollicitudin turpis. Vivamus aliquet elit sem, et ornare ex aliquam in. In cursus, felis non pretium molestie,</p>
</article>
<article class="step" style="left:623px">
  <h3><span class="step-num">3</span>Review</h3>
  <p>Morbi ultricies molestie orci. Aenean purus mauris, sodales nec diam dignissim, porttitor laoreet enim. Aliquam id sollicitudin turpis.</p>
  <p>Vivamus aliquet elit sem, et ornare ex aliquam in. In cursus, felis non pretium molestie, tellus lacus facilisis metus, ut accumsan nisi nulla accumsan risus.</p>
</article>
<article class="step" style="left:923px">
  <h3><span class="step-num">4</span>Contract</h3>
  <p>Aliquam id sollicitudin turpis. Vivamus aliquet elit sem, et ornare ex aliquam in. In cursus, felis non pretium molestie, tellus lacus facilisis metus, ut accumsan nisi nulla accumsan risus.</p>
</article>

<section class="season">
  <h2>New This Season</h2>
  <svg class="round-arrow prev" viewBox="0 0 42 42"><circle cx="21" cy="21" r="21" fill="#1e1664"/><path d="M24 13l-8 8 8 8" fill="none" stroke="#fff" stroke-width="4"/></svg>
  <div class="cover" style="left:111px;top:123px;width:216px;height:322px;background:linear-gradient(180deg,#2a2a2a 0%,#6b7a5a 40%,#b3987a 75%,#f4f1ea 100%)" role="img" aria-label="Book cover: fitness guide with photo collage"></div>
  <div class="cover" style="left:364px;top:123px;width:212px;height:322px;background:linear-gradient(180deg,#3a1b0e 0%,#a4582a 45%,#d8924a 70%,#6a9cc4 100%)" role="img" aria-label="Book cover: illustrated desert scene with figures"></div>
  <div class="cover" style="left:609px;top:123px;width:220px;height:270px;background:#1f1f1f" role="img" aria-label="Book cover: plain black poetry collection"></div>
  <div class="cover" style="left:863px;top:123px;width:218px;height:334px;background:linear-gradient(180deg,#8e1b1d,#6d1214)" role="img" aria-label="Book cover: deep red patterned cover"></div>
  <svg class="round-arrow next" viewBox="0 0 42 42"><circle cx="21" cy="21" r="21" fill="#1e1664"/><path d="M18 13l8 8-8 8" fill="none" stroke="#fff" stroke-width="4"/></svg>
</section>

<section class="testimonials">
  <h2>Testimonials</h2>
  <div class="quote" style="left:119px">
    <div class="quote-head"><div class="avatar"></div><div class="quote-name">John Doe<br>Author</div></div>
    <p>Lorem ipsum dolor sit amet, consectetur adipiscing elit. Morbi ultricies molestie orci. Aenean purus mauris, sodales nec diam dignissim, porttitor laoreet enim. Aliquam id sollicitudin</p>
  </div>
  <div class="quote" style="left:727px">
    <div class="quote-head"><div class="avatar"></div><div class="quote-name">John Doe<br>Author</div></div>
    <p>Lorem ipsum dolor sit amet, consectetur adipiscing elit. Morbi ultricies molestie orci. Aenean purus mauris, sodales nec diam dignissim, porttitor laoreet enim. Aliquam id sollicitudin</p>
  </div>
</section>

<div class="video" role="img" aria-label="Video thumbnail: collage about how books are published">
  <svg class="play" width="80" height="80" viewBox="0 0 80 80"><circle cx="40" cy="40" r="38" fill="#1e1664" stroke="#fff" stroke-width="3"/><path d="M31 24l26 16-26 16z" fill="#fff"/></svg>
</div>
<div class="video-caption">Learn How We Publish Books</div>

<h2 class="partners-title">Companies We Work With</h2>
<div class="partner" style="left:582px;top:3096px">Parcelry</div>
<div class="partner" style="left:872px;top:3096px">Hartwell &amp; Finch</div>
<div class="partner" style="left:582px;top:3183px">Pagefold</div>
<div class="partner" style="left:872px;top:3183px">Leafnest</div>
<div class="partner" style="left:582px;top:3269px">Lumo</div>
<div class="partner" style="left:872px;top:3269px">Tesso</div>

<footer class="site-footer">
  <div class="footer-brand">Brellow<br>Publishing</div>
  <ul class="footer-col" style="left:317px"><li>SUBMISSIONS</li><li>PRODUCTION</li><li>eBOOKS</li></ul>
  <ul class="footer-col" style="left:638px"><li>BOOKS</li><li>SEMINARS</li><li>PACKAGES</li></ul>
  <ul class="footer-col" style="left:900px"><li>AUTHORS</li><li>CONTACT</li><li>CAREERS</li></ul>
</footer>

</body>
</html>
```